Lucid Haven - Need Stationary Design

We need a stationary pack for our new Care company based in the uk
Are corporate colours are Pink and purple
Please use attached logo
Target Market(s)
The Care Industry
Industry/Entity Type
It Company
Contact Information for Business Card
Moira Blythe
Director

```html
<!DOCTYPE html>
<html lang="en">
<head>
<meta charset="utf-8">
<title>Lucid Haven – Stationery</title>
<link href="https://fonts.googleapis.com/css2?family=Questrial&family=EB+Garamond&display=swap" rel="stylesheet">
<style>
  :root {
    --purple: #7b3fa0;
    --pink: #e2308e;
    --paper: #ffffff;
    --flap: #dcdcdc;
    --ink: #2b2b2b;
    --backdrop: #1c1c1c;
    --sans: "Questrial", "Century Gothic", sans-serif;
    --serif: "EB Garamond", Georgia, serif;
  }
  * { margin: 0; padding: 0; box-sizing: border-box; }
  html, body { width: 1200px; height: 750px; overflow: hidden; background: var(--backdrop); }
  .canvas { position: relative; width: 1200px; height: 750px; }
  .sheet { position: absolute; background: var(--paper); box-shadow: 0 4px 14px rgba(0,0,0,.5); }

  .brand { position: absolute; display: flex; flex-direction: column; align-items: center; font-family: var(--sans); color: var(--purple); }
  .brand-dot { border-radius: 50%; background: var(--pink); }
  .brand-name { white-space: nowrap; }

  .contact { position: absolute; font-family: var(--sans); color: var(--purple); text-align: right; white-space: nowrap; }
  .contact b { font-weight: 400; color: var(--pink); }
  .contact .label { color: var(--purple); font-weight: 700; }

  /* Letterhead */
  .letterhead { left: 106px; top: 58px; width: 449px; height: 634px; }
  .letterhead .brand { left: 22px; top: 18px; width: 98px; }
  .letterhead .brand-dot { width: 22px; height: 22px; margin-bottom: 6px; }
  .letterhead .brand-name { font-size: 13px; }
  .letterhead .contact { right: 21px; top: 47px; font-size: 6.8px; line-height: 10.5px; }
  .letterhead .contact .company { font-weight: 700; color: var(--pink); font-size: 7px; }
  .contact .row span { margin-left: 12px; }
  .letter { position: absolute; left: 91px; width: 268px; font-family: var(--serif); color: var(--ink); font-size: 6.4px; line-height: 12px; }
  .letter-salutation { top: 178px; }
  .letter-body { top: 228px; text-align: justify; }
  .letter-body p + p { margin-top: 12px; }
  .letter-date { top: 409px; }

  /* Envelope */
  .envelope-front { left: 631px; top: 30px; width: 449px; height: 226px; }
  .envelope-front .brand { left: 20px; top: 28px; width: 94px; }
  .envelope-front .brand-dot { width: 18px; height: 18px; margin-bottom: 6px; }
  .envelope-front .brand-name { font-size: 12px; }
  .envelope-front .return { position: absolute; left: 19px; top: 101px; width: 98px; text-align: center; font-family: var(--sans); color: var(--purple); font-size: 3.6px; line-height: 6px; }
  .envelope-front .return strong { color: var(--pink); font-size: 4px; }
  .envelope-back { left: 631px; top: 284px; width: 448px; height: 224px; }
  .envelope-flap { position: absolute; left: 0; top: 0; width: 100%; height: 40px; }

  /* Business cards */
  .card-back { left: 611px; top: 546px; width: 225px; height: 145px; }
  .card-back .brand { left: 0; right: 0; top: 34px; }
  .card-back .brand-dot { width: 26px; height: 26px; margin-bottom: 8px; }
  .card-back .brand-name { font-size: 14px; }
  .card-front { left: 870px; top: 546px; width: 225px; height: 145px; }
  .card-front .brand { left: 12px; top: 16px; width: 70px; }
  .card-front .brand-dot { width: 16px; height: 16px; margin-bottom: 5px; }
  .card-front .brand-name { font-size: 8.5px; }
  .card-holder { position: absolute; right: 12px; top: 29px; text-align: right; font-family: var(--sans); }
  .card-holder-name { color: var(--purple); font-size: 8.6px; font-weight: 700; }
  .card-holder-role { color: var(--pink); font-size: 4px; margin-top: 1px; }
  .card-front .contact { right: 12px; top: 97px; font-size: 4.6px; line-height: 8px; }
  .card-front .contact .row span { margin-left: 8px; }
</style>
</head>
<body>
<main class="canvas">

  <section class="sheet letterhead">
    <div class="brand">
      <span class="brand-dot"></span>
      <span class="brand-name">Lucid Haven</span>
    </div>
    <address class="contact">
      <div class="company">Lucid Haven</div>
      <div>48 Elmfield Lane, Suite 12 &nbsp; London, GB 4820391</div>
      <div class="row"><span><span class="label">T</span> (+44) 201-5530</span><span><span class="label">F</span> (+44) 201-5531</span><span><span class="label">W</span> www.lucidhaven.uk</span></div>
    </address>
    <p class="letter letter-salutation">Dear Moira,</p>
    <div class="letter letter-body">
      <p>On the Graphics List the other day, I got the strangest request, for a dummy letter! Surely a letter is easy enough to fake, and not something I would have thought needed special dummy text. Perhaps I am ignorant, but I kind of assumed it was a joke. Except that it wasn't very funny. Unless I'm just too ignorant to understand it. Is there some sort of official dummy text for letters? I certainly find that "lorem ipsum" stuff incredibly useful for large documents, so I assume it could be used for a letter as well, but the designer (corporate funster, whatever) of course would have to make up his or her own date and name and address.</p>
      <p>I usually take the time to write utter bollocks a la automatic writing for something as short as a letter. As long as it doesn't have the word "bollocks" in it, it amuses me and helps prepare myself for the task athand. I usually take the time to write utter bollocks a la automatic writing for something as short as a letter. As long as it doesn't have the word "bollocks" in it, it amuses me and helps prepare myself for the task athand.</p>
    </div>
    <p class="letter letter-date">London, May 5th, 2016.</p>
  </section>

  <section class="sheet envelope-front">
    <div class="brand">
      <span class="brand-dot"></span>
      <span class="brand-name">Lucid Haven</span>
    </div>
    <address class="return"><strong>Lucid Haven</strong><br>48 Elmfield Lane, Suite 12 &nbsp; London, GB 4820391</address>
  </section>

  <section class="sheet envelope-back">
    <svg class="envelope-flap" viewBox="0 0 448 40" preserveAspectRatio="none" aria-hidden="true">
      <polygon points="0,0 448,0 422,40 26,40" fill="var(--flap)"/>
    </svg>
  </section>

  <section class="sheet card-back">
    <div class="brand">
      <span class="brand-dot"></span>
      <span class="brand-name">Lucid Haven</span>
    </div>
  </section>

  <section class="sheet card-front">
    <div class="brand">
      <span class="brand-dot"></span>
      <span class="brand-name">Lucid Haven</span>
    </div>
    <div class="card-holder">
      <div class="card-holder-name">Moira Blythe</div>
      <div class="card-holder-role">Director</div>
    </div>
    <address class="contact">
      <div>48 Elmfield Lane, Suite 12 &nbsp; London, GB 4820391</div>
      <div class="row"><span><span class="label">T</span> (+44) 201-5532</span><span><span class="label">F</span> (+44) 201-5531</span><span><span class="label">W</span> www.lucidhaven.uk</span></div>
      <div><span class="label">Email:</span> office@lucidhaven.uk</div>
    </address>
  </section>

</main>
</body>
</html>
```